New design for www.TrimSlotly.com

On TrimSlotly you can find & book your hairdresser. TrimSlotly is the biggest platform in the Netherlands.

- The design should be a responcive design
- Should be able to go global, should fit in perfectly between all the big booking platforms like roomqy, zipto etc,
- Should have te result of more bookings. :)
- We are ‘only’ asking a beautiful design, not a technical solution.
- We need a homepage (https://trimslotly.com/), search resultpage ((https://trimslotly.com/kapper/amsterdam/#), salonpage (https://trimslotly.com/kapper/vorden/mirelle-salon-studio/), about us page (https://trimslotly.com/aboutus/), for the hairdresser info page (https://trimslotly.com/kapper/), login/register page (https://trimslotly.com/account/signin/).

- On the page of the hairdresser there is a dynamic part. The part where you create your appointment. Please take a look at this part too after you choose your treatment (behandeling), employee (medewerker), Date (datum) and time (tijd). The part that you see after this, is the part where you fill in your data as a consumer.

I've added more logo's but mostly we use the green color.

A few of our competitors: www.glossmora.com, www.pelikora.com

Target Market(s)

All consumers

Industry/Entity Type

Hair And Beauty

Number of Pages Required

5+ page

Font styles to use
Sans Serif

Colors
abd036
c3c3c3
757575

Requirements
Must have
• Responsive
• We did an A/B test with the homepage. It turns out that option B works better then option A (take a look at the uploaded pictures). So what we need on the homepage: The USP's with the green checkboxes, The search button needs to by dynamic (changes for example from light green to dark green so you can see you can click it) The call to action sentence Zoek & Vind je kapsalon, the searchfield and searchbutton should be seperated.
Nice to have
• The style that we like is the flat design style. The website should be simple, clean and it should feel a bit like a luxury thing. Because an appointment with the hairdresser can be a real treat and luxury moment for yourself.
• The luxury feeling and flat design that is in the www.zipto.com website is really nice for example. But then it has to be a bit more light and not so black and dark.

```html
<!DOCTYPE html>
<html lang="en">
<head>
<meta charset="utf-8">
<title>TrimSlotly – Find &amp; book your hairdresser</title>
<link href="https://fonts.googleapis.com/css2?family=Open+Sans:wght@300;400;600;700&display=swap" rel="stylesheet">
<style>
:root{
  --green:#8dc63f;
  --green-dark:#6fa22d;
  --green-deep:#5d8a24;
  --ink:#333333;
  --grey:#757575;
  --grey-light:#c3c3c3;
  --paper:#ffffff;
  --mist:#eef0ee;
}
*{box-sizing:border-box;margin:0;padding:0}
html,body{width:1200px;height:2724px;overflow:hidden}
body{font-family:"Open Sans",Arial,sans-serif;color:var(--ink);background:var(--paper);position:relative}
section,header,footer{position:absolute;left:0;width:1200px}

/* hero */
.hero{top:0;height:600px}
.hero-photo{position:absolute;inset:0;background:linear-gradient(120deg,#5a4a3c 0%,#a89580 35%,#d8cfc3 55%,#8b7765 80%,#4a3d33 100%)}
.hero-shade{position:absolute;inset:0;background:rgba(20,20,20,.35)}
.brand{position:absolute;left:40px;top:26px;display:flex;align-items:center;gap:10px;color:#fff;font-weight:600;font-size:22px}
.brand-dot{width:26px;height:26px;border-radius:50%;background:var(--green)}
.nav{position:absolute;right:24px;top:22px;display:flex;list-style:none;background:rgba(255,255,255,.12)}
.nav li{padding:0 20px;line-height:40px;font-size:14px;color:#fff}
.nav li.active{background:var(--green);font-weight:600}
.search{position:absolute;left:352px;top:236px;display:flex;gap:8px}
.search-field{width:448px;height:52px;background:#fff;display:flex;align-items:center;padding:0 16px;gap:10px;color:#999;font-size:15px}
.search-btn{width:136px;height:52px;background:var(--green);color:#fff;font-size:18px;font-weight:600;display:flex;align-items:center;justify-content:center}
.search-links{position:absolute;left:352px;top:298px;width:592px;display:flex;font-size:13px;color:#fff}
.search-links .near{text-decoration:underline}
.search-links .right{margin-left:auto;display:flex;gap:20px}
.hero-actions{position:absolute;top:386px;left:472px;display:flex;gap:28px}
.btn{height:44px;padding:0 26px;display:flex;align-items:center;font-size:14px;font-weight:600;color:#fff}
.btn-fill{background:var(--green)}
.btn-line{border:2px solid #fff}
.slide-arrow{position:absolute;top:344px;width:38px;height:38px;background:#fff;display:flex;align-items:center;justify-content:center}
.slide-arrow.prev{left:92px}.slide-arrow.next{left:1070px}

/* welcome */
.welcome{top:600px;height:220px;text-align:center}
.section-title{color:var(--green);font-weight:300;font-size:44px}
.welcome .section-title{margin-top:36px}
.divider{width:60px;height:2px;background:var(--grey-light);margin:10px auto 18px}
.welcome p{width:640px;margin:0 auto;font-size:14px;line-height:22px;color:var(--grey)}

/* appointment */
.booking{top:820px;height:588px}
.booking-photo{position:absolute;inset:0;background:linear-gradient(90deg,#3b3f3a 0%,#5c6157 40%,#8a8a80 60%,#2f322e 100%)}
.booking-portrait{position:absolute;left:600px;top:0;width:600px;height:588px;background:radial-gradient(ellipse at 45% 45%,#f3d9c6 0%,#d9b49a 40%,#6b5a4e 80%,#3a3530 100%)}
.booking-form{position:absolute;left:88px;top:60px;width:400px;height:496px;background:rgba(240,245,232,.92);padding:24px 28px}
.booking-form h2{font-weight:400;font-size:26px;color:var(--green);text-align:center;margin-bottom:18px}
.field{margin-bottom:16px}
.field label{display:block;font-size:13px;color:var(--green-deep);font-weight:600;margin-bottom:6px}
.input{height:36px;background:#fff;border:1px solid #d6dccd;font-size:12px;color:#999;display:flex;align-items:center;padding:0 10px;justify-content:space-between}
.input.tall{height:72px;align-items:flex-start;padding-top:10px}
.booking-form .btn{margin:10px auto 0;width:120px;justify-content:center;height:40px}

/* steps */
.steps{top:1408px;height:464px;text-align:center}
.steps .section-title{margin-top:50px;font-weight:400;font-size:40px}
.step{position:absolute;top:176px;width:320px;text-align:center}
.step:nth-of-type(1){left:80px}.step:nth-of-type(2){left:440px}.step:nth-of-type(3){left:800px}
.step-icon{width:128px;height:128px;border-radius:50%;background:var(--green);margin:0 auto 20px;display:flex;align-items:center;justify-content:center;box-shadow:0 0 0 8px #eaf3dc}
.step h3{font-size:22px;font-weight:600;color:var(--green-deep);margin-bottom:8px}
.step p{font-size:13px;line-height:20px;color:var(--grey)}

/* stats */
.stats{top:1872px;height:228px;background:linear-gradient(90deg,#d9dcd8,#f1f2f0 50%,#d2d5d1)}
.stat{position:absolute;top:60px;width:200px;height:110px;background:rgba(255,255,255,.6);padding:18px 20px}
.stat strong{display:block;font-size:40px;font-weight:400;color:var(--green-dark);line-height:1}
.stat span{font-size:14px;color:var(--grey)}

/* partners */
.partners{top:2100px;height:228px}
.partner{position:absolute;top:96px;font-size:26px;font-weight:400;transform:translateX(-50%);white-space:nowrap}

/* footer */
.site-footer{top:2328px;height:396px;background:linear-gradient(180deg,#95c94c,#7fb538)}
.fcol{position:absolute;top:34px;color:#fff}
.fcol h4{font-size:18px;font-weight:600;margin-bottom:14px}
.fcol p{font-size:13px;line-height:21px}
.col-text{left:80px;width:300px}
.col-posts{left:460px;width:300px}
.col-search{left:820px;width:300px}
.socials{display:flex;gap:8px;margin-top:10px}
.socials span{width:26px;height:26px;border-radius:50%;background:rgba(255,255,255,.85)}
.post{display:flex;gap:8px;margin-bottom:12px;font-size:13px}
.post small{display:block;font-size:11px;opacity:.85}
.footer-search{height:36px;background:#fff;color:#999;font-size:13px;display:flex;align-items:center;padding:0 12px;margin-bottom:18px}
.contact{display:flex;align-items:center;gap:10px;font-size:13px;margin-bottom:12px}
.legal{position:absolute;left:0;bottom:0;width:1200px;height:34px;background:var(--green-deep);color:#fff;font-size:12px;text-align:center;line-height:34px}
</style>
</head>
<body>

<header class="hero">
  <div class="hero-photo" role="img" aria-label="Photo of a bright hair salon interior with stylists at work"></div>
  <div class="hero-shade"></div>
  <div class="brand"><span class="brand-dot"></span>TrimSlotly</div>
  <ul class="nav">
    <li class="active">Home</li><li>About us</li><li>Hair</li><li>Hair Removal</li><li>Massage</li><li>Nails</li><li>Spa</li><li>Contact us</li>
  </ul>
  <button class="slide-arrow prev" aria-label="Previous" style="border:0"><svg width="14" height="14" viewBox="0 0 14 14"><path d="M9 2 4 7l5 5" fill="none" stroke="#333" stroke-width="2"/></svg></button>
  <button class="slide-arrow next" aria-label="Next" style="border:0"><svg width="14" height="14" viewBox="0 0 14 14"><path d="M5 2l5 5-5 5" fill="none" stroke="#333" stroke-width="2"/></svg></button>
  <div class="search">
    <div class="search-field"><svg width="16" height="16" viewBox="0 0 16 16"><circle cx="7" cy="7" r="5" fill="none" stroke="#999" stroke-width="2"/><path d="M11 11l4 4" stroke="#999" stroke-width="2"/></svg>Search by city or zip code</div>
    <div class="search-btn">Search</div>
  </div>
  <div class="search-links"><span class="near">Or search near home</span><span class="right"><span>Map</span><span>All Distance</span></span></div>
  <div class="hero-actions"><span class="btn btn-fill">Login</span><span class="btn btn-line">Register</span></div>
</header>

<section class="welcome">
  <h1 class="section-title">Welcome</h1>
  <div class="divider"></div>
  <p>Find a salon near you, compare treatments and prices, read honest reviews from other guests and book your next appointment in a few clicks. Every salon on our platform is checked by our team, so you can sit back, relax and enjoy a real moment of luxury for yourself, any day of the week.</p>
</section>

<section class="booking">
  <div class="booking-photo" role="img" aria-label="Dimmed photo of a salon with styling chairs"></div>
  <div class="booking-portrait" role="img" aria-label="Portrait photo of a woman with fresh, glowing skin"></div>
  <form class="booking-form">
    <h2>Book An Appointment</h2>
    <div class="field"><label>Choose a day</label><div class="input">dd/mm/yyyy<svg width="14" height="14" viewBox="0 0 14 14"><rect x="1" y="2" width="12" height="11" fill="none" stroke="#8dc63f" stroke-width="1.5"/><path d="M1 5h12" stroke="#8dc63f" stroke-width="1.5"/></svg></div></div>
    <div class="field"><label>Choose Time</label><div class="input">Please choose a time<svg width="10" height="6" viewBox="0 0 10 6"><path d="M0 0l5 6 5-6z" fill="#999"/></svg></div></div>
    <div class="field"><label>Contact Method</label><div class="input">Please choose a method<svg width="10" height="6" viewBox="0 0 10 6"><path d="M0 0l5 6 5-6z" fill="#999"/></svg></div></div>
    <div class="field"><label>Observations</label><div class="input tall">Write your notes</div></div>
    <span class="btn btn-fill">Book Now</span>
  </form>
</section>

<section class="steps">
  <h2 class="section-title">How does it work?</h2>
  <div class="divider"></div>
  <div class="step">
    <div class="step-icon"><svg width="56" height="56" viewBox="0 0 56 56"><circle cx="24" cy="24" r="15" fill="none" stroke="#fff" stroke-width="5"/><path d="M35 35l14 14" stroke="#fff" stroke-width="6" stroke-linecap="round"/></svg></div>
    <h3>Search &amp; Find hairdresser</h3>
    <p>Type your city or postcode and browse trusted salons nearby. Compare prices, treatments and reviews to find the hairdresser that suits you best.</p>
  </div>
  <div class="step">
    <div class="step-icon"><svg width="56" height="56" viewBox="0 0 56 56"><rect x="6" y="10" width="44" height="40" fill="none" stroke="#fff" stroke-width="4"/><path d="M6 20h44M17 5v10M39 5v10" stroke="#fff" stroke-width="4"/><path d="M16 30h6M25 30h6M34 30h6M16 39h6M25 39h6" stroke="#fff" stroke-width="4"/></svg></div>
    <h3>Book your appointment</h3>
    <p>Pick a treatment, a stylist and a moment that fits your day. Your booking is confirmed at once and a reminder arrives before you go.</p>
  </div>
  <div class="step">
    <div class="step-icon"><svg width="56" height="56" viewBox="0 0 56 56"><path d="M10 29l12 12 24-26" fill="none" stroke="#fff" stroke-width="6" stroke-linecap="round" stroke-linejoin="round"/></svg></div>
    <h3>Enjoy your new hairstyle</h3>
    <p>Sit back and let the professionals take care of you. Afterwards, share a review to help other guests find their perfect salon.</p>
  </div>
</section>

<section class="stats">
  <div class="stat" style="left:70px"><strong>547</strong><span>Salons</span></div>
  <div class="stat" style="left:286px"><strong>16.028</strong><span>Treatments for booking</span></div>
  <div class="stat" style="left:502px"><strong>16.028</strong><span>Agreements</span></div>
  <div class="stat" style="left:718px"><strong>7.256</strong><span>Hairdressers booking</span></div>
  <div class="stat" style="left:934px"><strong>7.256</strong><span>Reliable reviews</span></div>
</section>

<section class="partners">
  <span class="partner" style="left:240px;color:#d81b60">Velora Hair</span>
  <span class="partner" style="left:468px;color:#7b3f8c">Ninette Rose</span>
  <span class="partner" style="left:690px;color:#b89a5a">Studio Ambre</span>
  <span class="partner" style="left:940px;color:#c2185b">Salon Liora</span>
</section>

<footer class="site-footer">
  <div class="fcol col-text">
    <h4>Text Widget</h4>
    <p>TrimSlotly brings the best salons of the country together in one place. Search, compare and book your hairdresser online, day and night, without waiting on the phone.</p>
    <h4 style="margin-top:22px">Get Social</h4>
    <div class="socials"><span></span><span></span><span></span><span></span><span></span><span></span><span></span></div>
  </div>
  <div class="fcol col-posts">
    <h4>Recent Posts</h4>
    <div class="post">›<span>Five easy looks for summer<small>June 12, 2015</small></span></div>
    <div class="post">›<span>How to care for coloured hair<small>May 28, 2015</small></span></div>
    <div class="post">›<span>Choosing the right stylist<small>May 14, 2015</small></span></div>
    <div class="post">›<span>A spa day in the city<small>April 30, 2015</small></span></div>
  </div>
  <div class="fcol col-search">
    <h4>Search Something</h4>
    <div class="footer-search">Search...</div>
    <div class="contact"><svg width="14" height="18" viewBox="0 0 14 18"><path d="M7 17S1 10 1 6.5a6 6 0 0 1 12 0C13 10 7 17 7 17z" fill="#fff"/><circle cx="7" cy="6.5" r="2.2" fill="#7fb538"/></svg>24 Keizersgracht Lane, Amsterdam 1015 NL</div>
    <div class="contact"><svg width="16" height="12" viewBox="0 0 16 12"><rect width="16" height="12" fill="#fff"/><path d="M0 0l8 7 8-7" fill="none" stroke="#7fb538" stroke-width="1.5"/></svg>hello@trimslotly.com</div>
    <div class="contact"><svg width="16" height="16" viewBox="0 0 16 16"><path d="M3 1l3 3-2 2a9 9 0 0 0 6 6l2-2 3 3-2 2C7 15 1 9 1 3z" fill="#fff"/></svg>(020) 555 0142</div>
  </div>
  <div class="legal">© 2015 TrimSlotly. All Rights Reserved</div>
</footer>

</body>
</html>
```